Boat Charter Power Point Template

Power Point Template for a Catalogue for a Boat Charter Company. In each slide there will be a main foto of the boat and then 3 mini photos plus all the aditional information of each boat. Here I attach 2 diferent presentations to get inspired

```html
<!DOCTYPE html>
<html lang="en">
<head>
<meta charset="utf-8">
<title>Boat Charter – Presentation Template</title>
<link href="https://fonts.googleapis.com/css2?family=Montserrat:wght@400;600;700&family=Satisfy&display=swap" rel="stylesheet">
<style>
:root{
  --navy:#1f3566;
  --panel:#f2f2f2;
  --white:#ffffff;
  --ink:#55585e;
  --canvas:#eeeeee;
}
*{margin:0;padding:0;box-sizing:border-box}
html,body{width:1200px;height:3606px;overflow:hidden}
body{background:var(--canvas);font-family:'Montserrat',Arial,sans-serif;color:var(--ink);position:relative}
.slide{position:absolute;width:560px;height:315px;background:var(--white);overflow:hidden;box-shadow:0 2px 8px rgba(0,0,0,.08)}
.l{left:29px}.r{left:610px}
.block{position:absolute;background:var(--navy)}
.photo{position:absolute}
.minis{position:absolute;display:flex;gap:4px}
.minis .photo{position:relative;flex:1;height:100%}
.yacht{background:linear-gradient(180deg,#bcc7d8 0%,#a6b5cc 46%,#4a6791 54%,#2a4470 100%)}
.sail{background:linear-gradient(135deg,#eef1f4 0%,#a9bdd3 55%,#2f5a8f 100%)}
.rope{background:linear-gradient(135deg,#ddd6cc 0%,#8d7c6a 50%,#463d35 100%)}
.deck{background:linear-gradient(160deg,#d3e3f2 0%,#4f86c0 55%,#eceeee 100%)}
.marina{background:linear-gradient(180deg,#5d7fb0 0%,#8ea8cc 40%,#dfe5ee 62%,#6a8fb9 80%,#24446f 100%)}
.panel{position:absolute;background:var(--panel)}
.script{font-family:'Satisfy',cursive;font-weight:400;color:var(--navy);font-size:28px;line-height:1}
.sub{font-size:6px;letter-spacing:4px;text-transform:uppercase;color:var(--navy);margin-top:8px}
.intro{font-size:5.5px;line-height:1.45;margin-top:8px}
.item{margin-bottom:9px}
.item h4{font-size:5.5px;font-weight:700;color:var(--navy);margin-bottom:2px}
.item p{font-size:5.5px;line-height:1.4}
.on-dark .script,.on-dark .sub,.on-dark .item h4{color:var(--white)}
.on-dark .intro,.on-dark .item p{color:rgba(255,255,255,.88)}
.caption{position:absolute;left:14px;bottom:12px;right:14px}
.caption .script{font-size:26px}
.pg{position:absolute;width:9px;height:9px;background:var(--navy);color:#fff;font-size:4px;text-align:center;line-height:9px}
.textbox{position:absolute}
.ruled{border-left:2px solid var(--navy);padding-left:12px}
.ruled-r{border-right:2px solid var(--navy);padding-right:12px;text-align:right}
.label{position:absolute;left:0;right:0;bottom:8px;text-align:center;font-size:6px;font-weight:600;color:#fff}
.cover{background:var(--navy)}
.cover .tint{position:absolute;inset:0;background:linear-gradient(90deg,rgba(31,53,102,.6),rgba(31,53,102,.35))}
.cover-title{position:absolute;left:0;right:0;text-align:center;color:#fff}
.cover-title .script{color:#fff}
.master-title{position:absolute;left:0;right:0;text-align:center}
.master-title .script{color:var(--navy)}
.web{font-size:6px;letter-spacing:5px;color:#fff;text-transform:uppercase}
.year{display:inline-block;border:1px solid #fff;border-radius:12px;padding:3px 14px;font-size:7px;color:#fff}
.contact{list-style:none}
.contact li{display:flex;align-items:center;gap:10px;font-size:7px;color:#fff;margin-bottom:9px}
.contact svg{width:11px;height:11px;flex:none}
.hero-main{left:160px;top:352px;width:880px;height:495px}
</style>
</head>
<body>

<section class="slide cover hero-main">
  <div class="photo marina" style="inset:0" role="img" aria-label="Large white motor yacht moored at a marina"></div>
  <div class="tint"></div>
  <div class="cover-title" style="top:28px"><p class="web">www.yourwebsite.com</p></div>
  <div class="cover-title" style="top:190px">
    <h1 class="script" style="font-size:86px">Boat Charter</h1>
    <p class="sub" style="color:#fff;font-size:10px;letter-spacing:7px;margin-top:14px">Subtitle goes here</p>
  </div>
  <div class="cover-title" style="bottom:28px"><span class="year" style="font-size:11px;padding:5px 22px;border-radius:16px">2021</span></div>
</section>

<!-- Row 1 -->
<section class="slide cover l" style="top:1222px">
  <div class="photo marina" style="inset:0" role="img" aria-label="Large white motor yacht moored at a marina"></div>
  <div class="tint"></div>
  <div class="cover-title" style="top:22px"><p class="web">www.yourwebsite.com</p></div>
  <div class="cover-title" style="top:124px">
    <h1 class="script" style="font-size:54px">Boat Charter</h1>
    <p class="sub" style="color:#fff;letter-spacing:5px">Subtitle goes here</p>
  </div>
  <div class="cover-title" style="bottom:18px"><span class="year">2021</span></div>
</section>

<section class="slide r" style="top:1222px">
  <div class="minis" style="left:0;top:0;width:560px;height:220px">
    <div class="photo marina" role="img" aria-label="Yacht bow at the dock, strip one"></div>
    <div class="photo marina" role="img" aria-label="Yacht hull, strip two"></div>
    <div class="photo marina" role="img" aria-label="Yacht hull, strip three"></div>
    <div class="photo marina" role="img" aria-label="Yacht cabin windows, strip four"></div>
    <div class="photo marina" role="img" aria-label="Yacht superstructure, strip five"></div>
    <div class="photo marina" role="img" aria-label="Yacht stern, strip six"></div>
    <div class="photo marina" role="img" aria-label="Marina buildings, strip seven"></div>
  </div>
  <div class="master-title" style="top:236px">
    <h2 class="script" style="font-size:38px">Boat Charter</h2>
    <p class="sub" style="margin-top:6px">Master slide presentation</p>
  </div>
</section>

<!-- Row 2 -->
<section class="slide l" style="top:1560px">
  <div class="block" style="left:0;top:0;width:250px;height:315px"></div>
  <div class="photo yacht" style="left:18px;top:18px;width:230px;height:282px" role="img" aria-label="White superyacht on open sea"></div>
  <div class="caption on-dark" style="left:30px;right:326px">
    <h2 class="script">Yacht Name</h2><p class="sub">Subtitle here</p>
    <p class="intro">Get a modern slide deck that is beautifully designed. Easy to change colors, photos and text. Impress your audience.</p>
  </div>
  <div class="minis" style="left:258px;top:18px;width:284px;height:88px">
    <div class="photo sail" role="img" aria-label="Sail against the sky"></div>
    <div class="photo rope" role="img" aria-label="Coiled deck ropes"></div>
    <div class="photo deck" role="img" aria-label="Bow deck over the sea"></div>
  </div>
  <div class="panel" style="left:258px;top:118px;width:284px;height:182px;padding:16px 22px">
    <div class="item"><h4>CONTENT TITLE 01</h4><p>Get a clean &amp; modern slide deck that is beautifully designed. Easy to change colors, photos and text.</p></div>
    <div class="item"><h4>CONTENT TITLE 02</h4><p>Get a clean &amp; modern slide deck that is beautifully designed. Easy to change colors, photos and text.</p></div>
    <div class="item"><h4>CONTENT TITLE 03</h4><p>Get a clean &amp; modern slide deck that is beautifully designed. Easy to change colors, photos and text.</p></div>
    <div class="item"><h4>CONTENT TITLE 04</h4><p>Get a clean &amp; modern slide deck that is beautifully designed. Easy to change colors, photos and text.</p></div>
  </div>
  <div class="pg" style="left:531px;top:296px">3</div>
</section>

<section class="slide r" style="top:1560px">
  <div class="block" style="left:310px;top:0;width:250px;height:315px"></div>
  <div class="photo yacht" style="left:312px;top:18px;width:230px;height:282px" role="img" aria-label="White superyacht on open sea"></div>
  <div class="caption on-dark" style="left:326px;right:30px;text-align:right">
    <h2 class="script">Yacht Name</h2><p class="sub">Subtitle here</p>
    <p class="intro">Get a modern slide deck that is beautifully designed. Easy to change colors, photos and text. Impress your audience.</p>
  </div>
  <div class="minis" style="left:18px;top:18px;width:284px;height:88px">
    <div class="photo sail" role="img" aria-label="Sail against the sky"></div>
    <div class="photo rope" role="img" aria-label="Coiled deck ropes"></div>
    <div class="photo deck" role="img" aria-label="Bow deck over the sea"></div>
  </div>
  <div class="panel" style="left:18px;top:118px;width:284px;height:182px;padding:16px 22px">
    <div class="item"><h4>CONTENT TITLE 01</h4><p>Get a clean &amp; modern slide deck that is beautifully designed. Easy to change colors, photos and text.</p></div>
    <div class="item"><h4>CONTENT TITLE 02</h4><p>Get a clean &amp; modern slide deck that is beautifully designed. Easy to change colors, photos and text.</p></div>
    <div class="item"><h4>CONTENT TITLE 03</h4><p>Get a clean &amp; modern slide deck that is beautifully designed. Easy to change colors, photos and text.</p></div>
    <div class="item"><h4>CONTENT TITLE 04</h4><p>Get a clean &amp; modern slide deck that is beautifully designed. Easy to change colors, photos and text.</p></div>
  </div>
  <div class="pg" style="left:20px;top:296px">4</div>
</section>

<!-- Row 3 -->
<section class="slide l" style="top:1897px">
  <div class="block" style="left:280px;top:0;width:280px;height:315px"></div>
  <div class="photo yacht" style="left:18px;top:22px;width:236px;height:132px" role="img" aria-label="White superyacht on open sea"></div>
  <div class="minis" style="left:258px;top:22px;width:284px;height:132px">
    <div class="photo sail" role="img" aria-label="Sail against the sky"></div>
    <div class="photo rope" role="img" aria-label="Coiled deck ropes"></div>
    <div class="photo deck" role="img" aria-label="Bow deck over the sea"></div>
  </div>
  <div class="panel" style="left:18px;top:154px;width:524px;height:144px"></div>
  <div class="textbox" style="left:38px;top:168px;width:200px">
    <div class="item"><h4>CONTENT TITLE 01</h4><p>Get a clean &amp; modern slide deck that is beautifully designed. Easy to change colors, photos and text.</p></div>
    <div class="item"><h4>CONTENT TITLE 02</h4><p>Get a clean &amp; modern slide deck that is beautifully designed. Easy to change colors, photos and text.</p></div>
    <div class="item"><h4>CONTENT TITLE 03</h4><p>Get a clean &amp; modern slide deck that is beautifully designed. Easy to change colors, photos and text.</p></div>
  </div>
  <div class="textbox ruled-r" style="right:38px;top:170px;width:200px">
    <h2 class="script">Yacht Name</h2><p class="sub">Subtitle here</p>
    <p class="intro">Get a modern slide deck that is beautifully designed. Easy to change colors, photos and text. Impress your audience.</p>
  </div>
  <div class="pg" style="left:20px;top:296px">6</div>
</section>

<section class="slide r" style="top:1897px">
  <div class="block" style="left:0;top:0;width:280px;height:315px"></div>
  <div class="minis" style="left:18px;top:22px;width:284px;height:132px">
    <div class="photo sail" role="img" aria-label="Sail against the sky"></div>
    <div class="photo rope" role="img" aria-label="Coiled deck ropes"></div>
    <div class="photo deck" role="img" aria-label="Bow deck over the sea"></div>
  </div>
  <div class="photo yacht" style="left:306px;top:22px;width:236px;height:132px" role="img" aria-label="White superyacht on open sea"></div>
  <div class="panel" style="left:18px;top:154px;width:524px;height:144px"></div>
  <div class="textbox ruled" style="left:38px;top:170px;width:200px">
    <h2 class="script">Yacht Name</h2><p class="sub">Subtitle here</p>
    <p class="intro">Get a modern slide deck that is beautifully designed. Easy to change colors, photos and text. Impress your audience.</p>
  </div>
  <div class="textbox" style="left:310px;top:168px;width:200px">
    <div class="item"><h4>CONTENT TITLE 01</h4><p>Get a clean &amp; modern slide deck that is beautifully designed. Easy to change colors, photos and text.</p></div>
    <div class="item"><h4>CONTENT TITLE 02</h4><p>Get a clean &amp; modern slide deck that is beautifully designed. Easy to change colors, photos and text.</p></div>
    <div class="item"><h4>CONTENT TITLE 03</h4><p>Get a clean &amp; modern slide deck that is beautifully designed. Easy to change colors, photos and text.</p></div>
  </div>
  <div class="pg" style="left:531px;top:296px">7</div>
</section>

<!-- Row 4 -->
<section class="slide l" style="top:2236px">
  <div class="block" style="left:0;top:0;width:250px;height:315px"></div>
  <div class="photo yacht" style="left:18px;top:18px;width:230px;height:282px" role="img" aria-label="White superyacht on open sea"></div>
  <div class="caption on-dark" style="left:30px;right:326px">
    <h2 class="script">Yacht Name</h2><p class="sub">Subtitle here</p>
    <p class="intro">Get a modern slide deck that is beautifully designed. Easy to change colors, photos and text. Impress your audience.</p>
  </div>
  <div class="panel" style="left:258px;top:18px;width:284px;height:182px;padding:16px 22px">
    <div class="item"><h4>CONTENT TITLE 01</h4><p>Get a clean &amp; modern slide deck that is beautifully designed. Easy to change colors, photos and text.</p></div>
    <div class="item"><h4>CONTENT TITLE 02</h4><p>Get a clean &amp; modern slide deck that is beautifully designed. Easy to change colors, photos and text.</p></div>
    <div class="item"><h4>CONTENT TITLE 03</h4><p>Get a clean &amp; modern slide deck that is beautifully designed. Easy to change colors, photos and text.</p></div>
    <div class="item"><h4>CONTENT TITLE 04</h4><p>Get a clean &amp; modern slide deck that is beautifully designed. Easy to change colors, photos and text.</p></div>
  </div>
  <div class="minis" style="left:258px;top:210px;width:284px;height:90px">
    <div class="photo sail" role="img" aria-label="Sail against the sky"></div>
    <div class="photo rope" role="img" aria-label="Coiled deck ropes"></div>
    <div class="photo deck" role="img" aria-label="Bow deck over the sea"></div>
  </div>
  <div class="pg" style="left:531px;top:10px">8</div>
</section>

<section class="slide r" style="top:2236px">
  <div class="block" style="left:310px;top:0;width:250px;height:315px"></div>
  <div class="photo yacht" style="left:312px;top:18px;width:230px;height:282px" role="img" aria-label="White superyacht on open sea"></div>
  <div class="caption on-dark" style="left:326px;right:30px;text-align:right">
    <h2 class="script">Yacht Name</h2><p class="sub">Subtitle here</p>
    <p class="intro">Get a modern slide deck that is beautifully designed. Easy to change colors, photos and text. Impress your audience.</p>
  </div>
  <div class="panel" style="left:18px;top:18px;width:284px;height:182px;padding:16px 22px">
    <div class="item"><h4>CONTENT TITLE 01</h4><p>Get a clean &amp; modern slide deck that is beautifully designed. Easy to change colors, photos and text.</p></div>
    <div class="item"><h4>CONTENT TITLE 02</h4><p>Get a clean &amp; modern slide deck that is beautifully designed. Easy to change colors, photos and text.</p></div>
    <div class="item"><h4>CONTENT TITLE 03</h4><p>Get a clean &amp; modern slide deck that is beautifully designed. Easy to change colors, photos and text.</p></div>
    <div class="item"><h4>CONTENT TITLE 04</h4><p>Get a clean &amp; modern slide deck that is beautifully designed. Easy to change colors, photos and text.</p></div>
  </div>
  <div class="minis" style="left:18px;top:210px;width:284px;height:90px">
    <div class="photo sail" role="img" aria-label="Sail against the sky"></div>
    <div class="photo rope" role="img" aria-label="Coiled deck ropes"></div>
    <div class="photo deck" role="img" aria-label="Bow deck over the sea"></div>
  </div>
  <div class="pg" style="left:20px;top:10px">9</div>
</section>

<!-- Row 5 -->
<section class="slide l" style="top:2573px">
  <div class="block" style="left:280px;top:0;width:280px;height:315px"></div>
  <div class="panel" style="left:18px;top:18px;width:524px;height:144px"></div>
  <div class="textbox" style="left:38px;top:32px;width:200px">
    <div class="item"><h4>CONTENT TITLE 01</h4><p>Get a clean &amp; modern slide deck that is beautifully designed. Easy to change colors, photos and text.</p></div>
    <div class="item"><h4>CONTENT TITLE 02</h4><p>Get a clean &amp; modern slide deck that is beautifully designed. Easy to change colors, photos and text.</p></div>
    <div class="item"><h4>CONTENT TITLE 03</h4><p>Get a clean &amp; modern slide deck that is beautifully designed. Easy to change colors, photos and text.</p></div>
  </div>
  <div class="textbox ruled-r" style="right:38px;top:34px;width:200px">
    <h2 class="script">Yacht Name</h2><p class="sub">Subtitle here</p>
    <p class="intro">Get a modern slide deck that is beautifully designed. Easy to change colors, photos and text. Impress your audience.</p>
  </div>
  <div class="photo yacht" style="left:18px;top:162px;width:236px;height:132px" role="img" aria-label="White superyacht on open sea"></div>
  <div class="minis" style="left:258px;top:162px;width:284px;height:132px">
    <div class="photo sail" role="img" aria-label="Sail against the sky"></div>
    <div class="photo rope" role="img" aria-label="Coiled deck ropes"></div>
    <div class="photo deck" role="img" aria-label="Bow deck over the sea"></div>
  </div>
  <div class="pg" style="left:20px;top:22px">10</div>
</section>

<section class="slide r" style="top:2573px">
  <div class="block" style="left:0;top:0;width:280px;height:315px"></div>
  <div class="panel" style="left:18px;top:18px;width:524px;height:144px"></div>
  <div class="textbox ruled" style="left:38px;top:34px;width:200px">
    <h2 class="script">Yacht Name</h2><p class="sub">Subtitle here</p>
    <p class="intro">Get a modern slide deck that is beautifully designed. Easy to change colors, photos and text. Impress your audience.</p>
  </div>
  <div class="textbox" style="left:310px;top:32px;width:200px">
    <div class="item"><h4>CONTENT TITLE 01</h4><p>Get a clean &amp; modern slide deck that is beautifully designed. Easy to change colors, photos and text.</p></div>
    <div class="item"><h4>CONTENT TITLE 02</h4><p>Get a clean &amp; modern slide deck that is beautifully designed. Easy to change colors, photos and text.</p></div>
    <div class="item"><h4>CONTENT TITLE 03</h4><p>Get a clean &amp; modern slide deck that is beautifully designed. Easy to change colors, photos and text.</p></div>
  </div>
  <div class="minis" style="left:18px;top:162px;width:284px;height:132px">
    <div class="photo sail" role="img" aria-label="Sail against the sky"></div>
    <div class="photo rope" role="img" aria-label="Coiled deck ropes"></div>
    <div class="photo deck" role="img" aria-label="Bow deck over the sea"></div>
  </div>
  <div class="photo yacht" style="left:306px;top:162px;width:236px;height:132px" role="img" aria-label="White superyacht on open sea"></div>
  <div class="pg" style="left:531px;top:22px">11</div>
</section>

<!-- Row 6 -->
<section class="slide l" style="top:2911px">
  <div class="photo yacht" style="left:18px;top:18px;width:250px;height:172px" role="img" aria-label="White superyacht on open sea">
    <p class="label">Add your text here</p>
  </div>
  <div class="minis" style="left:18px;top:198px;width:250px;height:100px">
    <div class="photo sail" role="img" aria-label="Sail against the sky"></div>
    <div class="photo rope" role="img" aria-label="Coiled deck ropes"></div>
    <div class="photo deck" role="img" aria-label="Bow deck over the sea"></div>
  </div>
  <div class="panel" style="left:282px;top:18px;width:260px;height:280px"></div>
  <div class="textbox ruled" style="left:312px;top:28px;width:210px">
    <h2 class="script">Yacht Name</h2><p class="sub">Subtitle here</p>
    <p class="intro">Get a modern slide deck that is beautifully designed. Easy to change colors, photos and text. Impress your audience.</p>
  </div>
  <div class="textbox" style="left:326px;top:148px;width:200px">
    <div class="item"><h4>CONTENT TITLE 01</h4><p>Get a clean &amp; modern slide deck that is beautifully designed. Easy to change colors, photos and text.</p></div>
    <div class="item"><h4>CONTENT TITLE 02</h4><p>Get a clean &amp; modern slide deck that is beautifully designed. Easy to change colors, photos and text.</p></div>
    <div class="item"><h4>CONTENT TITLE 03</h4><p>Get a clean &amp; modern slide deck that is beautifully designed. Easy to change colors, photos and text.</p></div>
  </div>
  <div class="pg" style="left:531px;top:296px">12</div>
</section>

<section class="slide r" style="top:2911px">
  <div class="panel" style="left:18px;top:18px;width:260px;height:280px"></div>
  <div class="textbox ruled" style="left:36px;top:28px;width:210px">
    <h2 class="script">Yacht Name</h2><p class="sub">Subtitle here</p>
    <p class="intro">Get a modern slide deck that is beautifully designed. Easy to change colors, photos and text. Impress your audience.</p>
  </div>
  <div class="textbox" style="left:50px;top:148px;width:200px">
    <div class="item"><h4>CONTENT TITLE 01</h4><p>Get a clean &amp; modern slide deck that is beautifully designed. Easy to change colors, photos and text.</p></div>
    <div class="item"><h4>CONTENT TITLE 02</h4><p>Get a clean &amp; modern slide deck that is beautifully designed. Easy to change colors, photos and text.</p></div>
    <div class="item"><h4>CONTENT TITLE 03</h4><p>Get a clean &amp; modern slide deck that is beautifully designed. Easy to change colors, photos and text.</p></div>
  </div>
  <div class="photo yacht" style="left:292px;top:18px;width:250px;height:172px" role="img" aria-label="White superyacht on open sea">
    <p class="label">Add your text here</p>
  </div>
  <div class="minis" style="left:292px;top:198px;width:250px;height:100px">
    <div class="photo sail" role="img" aria-label="Sail against the sky"></div>
    <div class="photo rope" role="img" aria-label="Coiled deck ropes"></div>
    <div class="photo deck" role="img" aria-label="Bow deck over the sea"></div>
  </div>
  <div class="pg" style="left:20px;top:296px">13</div>
</section>

<!-- Row 7 -->
<section class="slide cover l on-dark" style="top:3248px">
  <div class="photo marina" style="inset:0;opacity:.35" role="img" aria-label="Motor yacht moored at a marina, faded"></div>
  <div class="tint" style="background:rgba(31,53,102,.75)"></div>
  <div class="textbox ruled" style="left:22px;top:32px;width:220px;border-color:#fff">
    <h2 class="script">Yacht Name</h2><p class="sub">Subtitle here</p>
  </div>
  <p class="textbox intro" style="left:34px;top:112px;width:500px">Get a modern slide deck that is beautifully designed. Easy to change colors, photos and text. You can simply impress your audience and add a unique zing and appeal to your presentations.</p>
  <div class="minis" style="left:254px;top:16px;width:288px;height:82px">
    <div class="photo sail" role="img" aria-label="Sail against the sky"></div>
    <div class="photo rope" role="img" aria-label="Coiled deck ropes"></div>
    <div class="photo deck" role="img" aria-label="Bow deck over the sea"></div>
  </div>
  <div class="textbox" style="left:34px;top:178px;width:200px">
    <div class="item"><h4>CONTENT TITLE 01</h4><p>Get a clean &amp; modern slide deck that is beautifully designed. Easy to change colors, photos and text.</p></div>
    <div class="item"><h4>CONTENT TITLE 02</h4><p>Get a clean &amp; modern slide deck that is beautifully designed. Easy to change colors, photos and text.</p></div>
    <div class="item"><h4>CONTENT TITLE 03</h4><p>Get a clean &amp; modern slide deck that is beautifully designed. Easy to change colors, photos and text.</p></div>
  </div>
  <div style="position:absolute;left:272px;top:150px;width:1px;height:140px;background:rgba(255,255,255,.7)"></div>
  <div class="textbox" style="left:284px;top:178px;width:200px">
    <div class="item"><h4>CONTENT TITLE 04</h4><p>Get a clean &amp; modern slide deck that is beautifully designed. Easy to change colors, photos and text.</p></div>
    <div class="item"><h4>CONTENT TITLE 05</h4><p>Get a clean &amp; modern slide deck that is beautifully designed. Easy to change colors, photos and text.</p></div>
    <div class="item"><h4>CONTENT TITLE 06</h4><p>Get a clean &amp; modern slide deck that is beautifully designed. Easy to change colors, photos and text.</p></div>
  </div>
</section>

<section class="slide cover r" style="top:3248px">
  <div class="photo marina" style="inset:0" role="img" aria-label="Motor yacht moored at a marina"></div>
  <div class="tint" style="background:rgba(31,53,102,.7)"></div>
  <div style="position:absolute;left:52px;top:72px;width:130px;height:1px;background:#fff"></div>
  <h3 class="script" style="position:absolute;left:52px;top:80px;color:#fff;font-size:26px">Contact Us</h3>
  <h2 class="script" style="position:absolute;right:48px;top:132px;color:#fff;font-size:58px">Thank You</h2>
  <ul class="contact" style="position:absolute;left:60px;top:208px">
    <li><svg viewBox="0 0 24 24" fill="#fff"><path d="M6.6 10.8a15.1 15.1 0 006.6 6.6l2.2-2.2a1 1 0 011-.25 11.4 11.4 0 003.6.57 1 1 0 011 1V20a1 1 0 01-1 1A17 17 0 013 4a1 1 0 011-1h3.5a1 1 0 011 1c0 1.25.2 2.45.57 3.6a1 1 0 01-.25 1z"/></svg>+1 234 567 890</li>
    <li><svg viewBox="0 0 24 24" fill="none" stroke="#fff" stroke-width="2"><circle cx="12" cy="12" r="9"/><path d="M3 12h18M12 3c3 3 3 15 0 18M12 3c-3 3-3 15 0 18"/></svg>www.yourwebsite.com</li>
    <li><svg viewBox="0 0 24 24" fill="none" stroke="#fff" stroke-width="2"><rect x="3" y="5" width="18" height="14"/><path d="M4 6.5l8 6 8-6"/></svg>addyouremail@here.com</li>
    <li><svg viewBox="0 0 24 24" fill="#fff"><path d="M12 2a7 7 0 00-7 7c0 5 7 13 7 13s7-8 7-13a7 7 0 00-7-7zm0 9.5A2.5 2.5 0 1112 6.5a2.5 2.5 0 010 5z"/></svg>Add your location here</li>
  </ul>
</section>

</body>
</html>
```